India March 15 Flyer

I would like a A4 Flyer made.
Very similair to attached file but the following changes
Name would be Explore Kerivan Weaving & Spice Journey

Cost $6995.00pp
16days fully escorted
Breakfast & Dinner included for 15days
Tour Departs Auckland 15th March 2015

Take out anything that is associated to Brisket Globe Voyages and it should be QMTrip Agents (attached) file for this.
Also no address just phone no's which is
09 573 8162
021736194
merel@qmtripagents.example.co.nz
QMTrip Agents Support Office:
Level 3, Pellor Finance Spire, 22-30 Quillane Rd,
Palmerston North 4493
Web:www.qmtripagents.example.co.nz
Under conditions take out Brisket Globe Voyages and put in QMTrip Agents and prices correct as at 20August 2014.
Under Conditions please change $400 deposit to $500 deposit pp.
Under Conditions: Price is Share Twin. Please advise if you want a single supplement cost.
I have attached a flyer that was done for me when i did the last tour. So this will give you an idea.
Also have attached the current itinerary that we will be doing for the March 2015 tour.
Hope this is enough information

Hello, Please do not forget to do the back of the flyer. dont put in itinerary but maybe a picture of the region that we are traveling and the Terms and Conditions which is so important. Thanks

I have noticed that the designs comming through dont have fully escorted by Merel Danforth which is a part of the brief with the flyer I included. Also return flights etc. Everything that was on the orginal flyer needs to include all of this except the Brisket Globe Voyages.

as this is a textile and culinary tour i would like to see pictures of textiles and food, as well as the normal pictures of India. I only seem to be getting elephant, taj extra but need to show the tour i am selling. Many thanks

Please re read the brief as i have made the required changes on this. IE: Price is now changed as well as some Terms and Conditions

• About Merel Danforth
• Pictures of Textiles and Culinerary as well as monuments

```html
<!DOCTYPE html>
<html lang="en">
<head>
<meta charset="utf-8">
<title>Explore Kerivan Weaving & Spice Journey – Flyer</title>
<link href="https://fonts.googleapis.com/css2?family=Lato:wght@400;700;900&display=swap" rel="stylesheet">
<style>
:root{
  --green:#22b04b;
  --green-soft:#dff1e3;
  --ink:#231f20;
  --white:#ffffff;
  --backdrop:#ececec;
  --photo-warm-a:#c8432a;
  --photo-warm-b:#e6b25a;
  --photo-teal:#2f6f73;
}
*{box-sizing:border-box;margin:0;padding:0}
html,body{width:1200px;height:860px;overflow:hidden}
body{background:var(--backdrop);font-family:'Lato',Arial,sans-serif;color:var(--ink);position:relative}

.page{position:absolute;background:var(--green);box-shadow:0 2px 8px rgba(0,0,0,.25)}
.page--front{left:25px;top:18px;width:566px;height:790px}
.page--back{left:612px;top:55px;width:560px;height:786px}

/* front */
.hero-photo{position:absolute;left:15px;top:14px;width:530px;height:528px;border-radius:22px 22px 0 0;
  background:radial-gradient(ellipse at 60% 45%,var(--photo-warm-a) 0%,#9a2a1c 30%,transparent 55%),
  linear-gradient(160deg,var(--photo-warm-b) 0%,#b86a3a 35%,var(--photo-teal) 75%,#274a4a 100%)}
.title-callout{position:absolute;left:0;top:0;width:566px;height:560px;pointer-events:none}
.title-callout svg{position:absolute;left:0;top:0}
.title-callout .heading{position:absolute;left:56px;top:398px;transform:rotate(-13deg);transform-origin:left top;color:var(--white);font-weight:900;line-height:1;white-space:nowrap}
.heading__main{display:block;font-size:31px}
.heading__sub{display:block;font-size:22px;margin:7px 0 0 10px;font-weight:700}

.intro{position:absolute;left:32px;top:566px;width:238px;color:var(--white);font-size:10.8px;line-height:1.42}

.price-box{position:absolute;left:277px;top:470px;width:245px;height:207px;background:var(--green);border-radius:14px;color:var(--white);padding:8px 18px 6px}
.price{text-align:center;font-weight:900;font-size:46px;line-height:.95}
.price sup{font-size:22px;vertical-align:18px}
.price small{font-size:10px;font-weight:700}
.price-note{text-align:center;font-weight:700;font-size:12.5px;margin-top:2px}
.includes-label{font-size:8px;font-weight:700;margin-top:6px}
.includes{display:grid;grid-template-columns:1fr 1fr;column-gap:10px;row-gap:3px;list-style:none;font-size:9px;line-height:1.25;margin-top:1px}
.includes li{padding-left:8px;position:relative}
.includes li::before{content:"";position:absolute;left:0;top:4px;width:4px;height:4px;border-radius:50%;background:var(--white)}
.depart{font-size:9px;margin-top:6px}

.contact-strip{position:absolute;left:15px;top:642px;width:530px;height:134px;background:var(--white);border-radius:0 0 22px 22px}
.contact{position:absolute;font-weight:700;line-height:1.35}
.contact__name{font-size:12.5px;color:var(--ink)}
.contact__line{font-size:12.5px;color:var(--green);margin-top:7px}
.page--front .contact{left:18px;top:58px}
.brand{position:absolute;display:flex;align-items:center;gap:6px}
.brand__dot{width:22px;height:22px;border-radius:50%;background:var(--green)}
.brand__name{font-weight:900;font-size:19px;color:var(--ink)}
.page--front .brand{left:345px;top:86px}

/* back */
.back-panel{position:absolute;left:16px;top:13px;width:528px;height:760px;background:var(--white);border-radius:22px}
.itinerary{position:absolute;left:8px;top:15px;width:242px}
.itinerary__title{background:var(--ink);color:var(--white);font-size:9px;font-weight:700;padding:5px 5px;margin-bottom:1px}
.day{padding:3px 3px;font-size:6.9px;line-height:1.38}
.day:nth-child(even){background:var(--green-soft)}
.day b{display:block;font-size:7.5px}
.photo{position:absolute;left:262px;width:250px;height:192px}
.photo--monument{top:15px;background:linear-gradient(180deg,#b9c5c9 0%,#e8d6b0 55%,#b06a3a 80%,#6a3a22 100%)}
.photo--desert{top:222px;background:radial-gradient(circle at 78% 42%,#ffe9a0 0%,#f6a431 8%,transparent 20%),linear-gradient(180deg,#d9551f 0%,#f2902d 55%,#6b2c10 85%,#2b1006 100%)}
.photo--fort{top:429px;background:linear-gradient(180deg,#7fb1e0 0%,#a9cbe8 30%,#b5553a 55%,#8c3a27 80%,#c9b8a0 100%)}
.terms{position:absolute;left:8px;top:630px;width:512px;font-size:6.2px;line-height:1.45}
.page--back .contact{left:18px;top:684px}
.page--back .contact__line{margin-top:6px}
.page--back .brand{left:340px;top:700px}
</style>
</head>
<body>

<section class="page page--front" aria-label="Flyer front">
  <div class="hero-photo" role="img" aria-label="Close-up of painted wooden elephant figurines on colourful Indian textile"></div>

  <div class="title-callout">
    <svg width="566" height="560" viewBox="0 0 566 560" aria-hidden="true">
      <polygon points="27,374 285,312 323,270 317,305 345,298 366,424 53,502" fill="var(--ink)" stroke="var(--white)" stroke-width="3"/>
    </svg>
    <h1 class="heading">
      <span class="heading__main">Explore Kerivan</span>
      <span class="heading__sub">Weaving &amp; Spice Journey</span>
    </h1>
  </div>

  <p class="intro">India is one of the most captivating countries on earth - from its rich culture to breathtaking scenery. A trip to India will create memories to last you a lifetime.</p>

  <div class="contact-strip">
    <div class="contact">
      <p class="contact__name">QMTrip Agents</p>
      <p class="contact__line">Ph: 09 573 8162 &nbsp;| &nbsp;02 173 6194</p>
      <p class="contact__line">E: merel@qmtripagents.example.co.nz</p>
    </div>
    <div class="brand"><span class="brand__dot"></span><span class="brand__name">QMTrip Agents</span></div>
  </div>

  <div class="price-box">
    <p class="price"><sup>$</sup>6995<small>PP</small></p>
    <p class="price-note">16 day fully escorted tour</p>
    <p class="includes-label">INCLUDES</p>
    <ul class="includes">
      <li>Return flights on Corvane Airlines in Economy Class</li>
      <li>Local transport &amp; transfers</li>
      <li>15 nights accommodation</li>
      <li>Sightseeing &amp; entry fees to selected monuments</li>
      <li>Fully escorted by Merel Danforth</li>
      <li>Breakfast &amp; Dinner included</li>
    </ul>
    <p class="depart">Tour departs Auckland 15th March 2015</p>
  </div>
</section>

<section class="page page--back" aria-label="Flyer back">
  <div class="back-panel">
    <div class="itinerary">
      <h2 class="itinerary__title">ITINERARY OVERVIEW</h2>
      <div class="days">
        <div class="day"><b>Day 01: Arrive Delhi (Flight: TBA) (Normal Check in 1200 Hrs.)</b>We arrive at Delhi International Airport.</div>
        <div class="day"><b>Day 02: In Delhi</b>Enjoy buffet breakfast at the hotel. Assemble at the hotel lobby and Merel (tour manager) will discuss your tour program.</div>
        <div class="day"><b>Day 03: Delhi – Lucknow<br>(Flight: KV 312 ETD 1240 hrs. / ETA 1345 hrs.)</b>After buffet breakfast at the hotel, transfer to Delhi airport to board flight to Lucknow.</div>
        <div class="day"><b>Day 04: Lucknow</b>Enjoy breakfast at the hotel and we visit a Chikan workshop and watch skilled karigars (workers) delicately working on unique styles and stitches.</div>
        <div class="day"><b>Day 05: Lucknow – Varanasi<br>(Train: Intercity Express ETD 0700 hrs. / ETA 1330 hrs.)</b>Early morning transfer to Lucknow railway station to board train to Varanasi.</div>
        <div class="day"><b>Day 06: Varanasi – Agra<br>(Desert Link Express ETD 1720 ETA 0610 Next day)</b>Wake up early morning around 0530 hrs. and proceed to enjoy the sunrise boat ride on river Ganges.</div>
        <div class="day"><b>Day 07: Arrive Agra (ETD 0610)</b>Morning arrive Agra, transfer to the hotel.</div>
        <div class="day"><b>Day 08: Agra</b>This morning, shortly before sunrise at 06:31, we'll head out for a sun rise visit to the Taj Mahal.</div>
        <div class="day"><b>Day 09: Agra – Jaipur<br>(Distance: 260 kms / Driving Time: Approx. 5 hours)</b>After breakfast check out of the hotel and travel towards Jaipur the Pink City of India.</div>
        <div class="day"><b>Day 10: Jaipur</b>After buffet breakfast, enjoy guided city tour and visit Amber Fort</div>
        <div class="day"><b>Day 11: Jaipur</b>Enjoy buffet breakfast at the hotel.</div>
        <div class="day"><b>Day 12: Jaipur – Jodhpur<br>(Distance: 330 kms / Driving Time: Approx. 7 hours)</b>After buffet breakfast, travel to Jodhpur.</div>
        <div class="day"><b>Day 13: Jodhpur</b>Have a leisurely breakfast and proceed for sightseeing tour.</div>
        <div class="day"><b>Day 14: Jodhpur – Ranakpur – Udaipur<br>(Distance: 290 kms / Driving Time: Approx 6 hours)</b>After buffet breakfast, drive to Udaipur, en-route pass lush green valleys, streams and heart capturing views before visiting Ranakpur.</div>
        <div class="day"><b>Day 15: Udaipur</b>After buffet breakfast, enjoy city tour of Udaipur.</div>
        <div class="day"><b>Day 16: Udaipur – Mumbai (Flight TBA)</b>After a leisurely breakfast check out from the hotel at 1200 hrs.</div>
      </div>
    </div>

    <div class="photo photo--monument" role="img" aria-label="White marble domed mausoleum with minarets reflected in water at dusk"></div>
    <div class="photo photo--desert" role="img" aria-label="Camel caravan silhouetted against an orange desert sunset"></div>
    <div class="photo photo--fort" role="img" aria-label="Red sandstone fort walls and gateway under blue sky"></div>

    <p class="terms"><b>Terms &amp; Conditions:</b> The price quoted for the land, airfare and taxes are subject to change without notice until final payment has been received in full and tickets are issued. - Deposit is non refundable and due within 7 days of the invoice dates (unless otherwise stated) Deposit required is $500 per person. - Receiving confirmation of the booking means you and you have read and agreed on QMTrip Agents booking conditions attached. Due to any unforeseen circumstances booking conditions may change without notice hence please request a copy before making reservation.</p>

    <div class="contact">
      <p class="contact__name">QMTrip Agents</p>
      <p class="contact__line">Ph: 09 573 8162 &nbsp;| &nbsp;02 173 6194</p>
      <p class="contact__line">E: merel@qmtripagents.example.co.nz</p>
    </div>
    <div class="brand"><span class="brand__dot"></span><span class="brand__name">QMTrip Agents</span></div>
  </div>
</section>

</body>
</html>
```